Veterinary Business cards

Redesign Business Card

Information needed on Card:
Hours: MON-FRI: 3PM -11PM; SAT- SUN- 9 AM- 6PM
Help@bayfernvet.com
www.bayfernvet.com
555-718-2946
4173 SE 19th Ave. rvd, wa 73958
*No appointment necessary*

Optional:
Our tag line is "We're here when you need us" - If it fits on the cards.

```html
<!DOCTYPE html>
<html lang="en">
<head>
<meta charset="utf-8">
<title>Bayfern Vet Urgent Care – Business Cards</title>
<link rel="stylesheet" href="https://fonts.googleapis.com/css2?family=Cormorant+Garamond:ital,wght@1,600&family=Marcellus&family=Montserrat:wght@500;600&display=swap">
<style>
  :root {
    --navy: #173e6a;
    --orange: #f4922a;
    --peach: #f7e4d3;
    --paper: #ffffff;
    --stage: #3a3636;
    --card-w: 860px;
    --card-h: 480px;
  }
  * { box-sizing: border-box; margin: 0; padding: 0; }
  html, body { width: 1200px; height: 1200px; overflow: hidden; }
  body {
    background: var(--stage);
    display: flex;
    flex-direction: column;
    align-items: center;
    justify-content: center;
    gap: 60px;
  }
  .card {
    position: relative;
    width: var(--card-w);
    height: var(--card-h);
    background: var(--paper);
    overflow: hidden;
  }
  .card__pattern {
    position: absolute;
    inset: 0 0 92px 0;
    background:
      radial-gradient(ellipse 34% 48% at 82% 45%, var(--peach) 0%, rgba(247,228,211,0.55) 60%, rgba(255,255,255,0) 100%),
      linear-gradient(180deg, #fffaf6 0%, #fdf3ea 100%);
  }
  .card__band {
    position: absolute;
    left: 0; right: 0;
    top: 380px;
    height: 78px;
  }
  .band__rule {
    position: absolute;
    left: 0; right: 0;
    height: 7px;
    background: var(--orange);
  }
  .band__rule--top { top: 0; }
  .band__rule--bottom { top: 71px; }
  .band__bar {
    position: absolute;
    left: 0; right: 0;
    top: 13px;
    height: 51px;
    background: var(--navy);
    color: var(--paper);
    display: flex;
    align-items: center;
    justify-content: center;
  }
  .hours {
    font-family: "Montserrat", sans-serif;
    font-weight: 600;
    font-size: 24px;
    letter-spacing: 0.2px;
    white-space: nowrap;
  }
  .website {
    font-family: "Montserrat", sans-serif;
    font-weight: 500;
    font-size: 24px;
    letter-spacing: 3.5px;
  }
  .brand {
    display: flex;
    align-items: center;
    gap: 18px;
    color: var(--navy);
    font-family: "Marcellus", serif;
    white-space: nowrap;
  }
  .brand__dot {
    border-radius: 50%;
    background: var(--orange);
    flex: none;
  }
  .card--front .brand {
    position: absolute;
    left: 0; right: 0;
    top: 150px;
    justify-content: center;
    font-size: 72px;
  }
  .card--front .brand__dot { width: 48px; height: 48px; }
  .card--back .brand {
    position: absolute;
    left: 82px;
    top: 78px;
    font-size: 42px;
    gap: 12px;
  }
  .card--back .brand__dot { width: 28px; height: 28px; }
  .contact {
    position: absolute;
    left: 84px;
    top: 210px;
    list-style: none;
    color: var(--navy);
    font-family: "Montserrat", sans-serif;
    font-weight: 500;
    font-size: 19px;
    letter-spacing: 1.6px;
    line-height: 30px;
  }
  .tagline {
    position: absolute;
    right: 40px;
    top: 96px;
    width: 360px;
    text-align: center;
    color: var(--navy);
    font-family: "Cormorant Garamond", serif;
    font-style: italic;
    font-weight: 600;
    font-size: 56px;
    line-height: 68px;
    text-transform: uppercase;
  }
</style>
</head>
<body>

  <section class="card card--front" aria-label="Business card front">
    <div class="card__pattern" role="img" aria-label="Soft peach paw print pattern background"></div>
    <div class="brand">
      <span class="brand__dot" aria-hidden="true"></span>
      <span class="brand__name">BAYFERN VET</span>
    </div>
    <div class="card__band">
      <div class="band__rule band__rule--top"></div>
      <div class="band__bar"><p class="hours">MON-FRI: 3PM -11PM; SAT- SUN- 9 AM- 6PM</p></div>
      <div class="band__rule band__rule--bottom"></div>
    </div>
  </section>

  <section class="card card--back" aria-label="Business card back">
    <div class="card__pattern" role="img" aria-label="Soft peach paw print pattern background"></div>
    <div class="brand">
      <span class="brand__dot" aria-hidden="true"></span>
      <span class="brand__name">BAYFERN VET</span>
    </div>
    <ul class="contact">
      <li>4173 SE 19th Ave. rvd,</li>
      <li>wa 73958</li>
      <li>555-718-2946</li>
      <li>Help@bayfernvet.com</li>
    </ul>
    <p class="tagline">“We're here when you need us”</p>
    <div class="card__band">
      <div class="band__rule band__rule--top"></div>
      <div class="band__bar"><p class="website">www.bayfernvet.com</p></div>
      <div class="band__rule band__rule--bottom"></div>
    </div>
  </section>

</body>
</html>
```